Verdanix Medical Business Card

Create a high class Business card for Medical Aesthetics and Wellness Practice called Verdanix Medical Aesthetics and Wellness as per the logo attached.
Addresss is: 418 Harlan Brook Road Suite 312 Melville, New York 11093
Phone (555)204-7391 IG @verdanix_medical
Verdanixmedical.example

I need 5 different name configurations
1) Dr. Theo Valcourt
Aesthetics and Wellness Specialist
Medical Director

2) Rosalind Pettinger, NP
Clinical Nurse Manager

3) Marla Vostrik, RN
Aesthetic Nurse Specialist

4) Petra Halvesen, RN

5) Dana Kowbeck, L.E.
Senior Licensed Esthetician

Target Market(s)

22-55 Females

Industry/Entity Type

Medical Spa and Wellness

Contact Information for Business Card

Logo, address, phone, web, instagram, providers name

Requirements
Must have
• Attractive classy modern look

```html
<!DOCTYPE html>
<html lang="en">
<head>
<meta charset="utf-8">
<title>Verdanix Medical Business Card</title>
<link href="https://fonts.googleapis.com/css2?family=Bodoni+Moda:wght@400&family=Cinzel:wght@400&family=Source+Serif+4:wght@400;500&display=swap" rel="stylesheet">
<style>
  :root {
    --page: #e4e4e4;
    --ink-black: #0b0b0b;
    --paper: #ffffff;
    --text-light: #f4f4f4;
    --text-dark: #222222;
    --text-muted: #555555;
    --accent-teal: #2c4f5b;
    --rule: #8a8a8a;
  }
  * { margin: 0; padding: 0; box-sizing: border-box; }
  html, body {
    width: 1200px; height: 1200px; overflow: hidden;
    background: var(--page);
  }
  .card {
    position: absolute;
    left: 178px;
    width: 845px;
    height: 479px;
  }
  .card--front { top: 99px; background: var(--ink-black); color: var(--text-light); }
  .card--back { top: 629px; background: var(--paper); color: var(--text-dark); }

  .brand { position: absolute; left: 0; right: 0; text-align: center; }
  .brand__name {
    font-family: "Bodoni Moda", serif;
    font-weight: 400;
    letter-spacing: 0.06em;
    line-height: 1;
  }
  .brand__tagline {
    font-family: "Cinzel", serif;
    letter-spacing: 0.02em;
    line-height: 1.2;
  }
  .brand__city {
    font-family: "Cinzel", serif;
    letter-spacing: 0.5em;
    line-height: 1.2;
  }

  .card--front .brand { top: 178px; }
  .card--front .brand__name { font-size: 50px; }
  .card--front .brand__tagline { font-size: 20px; margin-top: 26px; }
  .card--front .brand__city { font-size: 12px; margin-top: 14px; }

  .identity {
    position: absolute; left: 132px; top: 146px; width: 308px;
    text-align: center;
  }
  .identity .brand { position: static; }
  .identity .brand__name { font-size: 37px; color: var(--text-dark); }
  .identity .brand__tagline { font-size: 14px; margin-top: 14px; color: var(--text-dark); }
  .identity .brand__city { font-size: 9px; margin-top: 8px; color: var(--text-dark); }
  .person__name {
    font-family: "Source Serif 4", serif; font-weight: 500;
    font-size: 33px; line-height: 1.1; color: var(--accent-teal); margin-top: 10px;
  }
  .person__role {
    font-family: "Source Serif 4", serif;
    font-size: 15.5px; line-height: 21px; color: var(--text-muted); margin-top: 6px;
  }

  .divider {
    position: absolute; left: 452px; top: 151px; width: 1px; height: 180px;
    background: var(--rule);
  }

  .contact {
    position: absolute; left: 468px; top: 150px;
    font-family: "Source Serif 4", serif; font-size: 16px;
    letter-spacing: 0.04em; color: var(--text-muted);
    list-style: none;
  }
  .contact__item { display: flex; align-items: flex-start; height: 30px; }
  .contact__item--address { margin-top: 18px; line-height: 27px; height: auto; }
  .contact__icon { width: 20px; height: 20px; margin-right: 14px; flex: none; margin-top: 2px; }
  .contact__icon--square { width: 15px; height: 15px; margin: 4px 17px 0 2px; border: 2px solid var(--accent-teal); }
</style>
</head>
<body>

<section class="card card--front" aria-label="Card front">
  <div class="brand">
    <div class="brand__name">verdanix</div>
    <div class="brand__tagline">MEDICAL AESTHETICS AND WELLNESS</div>
    <div class="brand__city">NEW YORK</div>
  </div>
</section>

<section class="card card--back" aria-label="Card back">
  <div class="identity">
    <div class="brand">
      <div class="brand__name">verdanix</div>
      <div class="brand__tagline">MEDICAL AESTHETICS AND WELLNESS</div>
      <div class="brand__city">NEW YORK</div>
    </div>
    <div class="person__name">Dr. Theo Valcourt</div>
    <div class="person__role">Aesthetics and Wellness Specialist<br>Medical Director</div>
  </div>

  <div class="divider"></div>

  <ul class="contact">
    <li class="contact__item">
      <svg class="contact__icon" viewBox="0 0 24 24" aria-hidden="true">
        <path fill="#2c4f5b" d="M6.6 10.8a15.1 15.1 0 0 0 6.6 6.6l2.2-2.2a1 1 0 0 1 1-.25 11.4 11.4 0 0 0 3.6.57 1 1 0 0 1 1 1V20a1 1 0 0 1-1 1A17 17 0 0 1 3 4a1 1 0 0 1 1-1h3.5a1 1 0 0 1 1 1c0 1.250.2 2.45.57 3.6a1 1 0 0 1-.25 1z"/>
      </svg>
      (555)204-7391
    </li>
    <li class="contact__item">
      <svg class="contact__icon" viewBox="0 0 24 24" aria-hidden="true">
        <rect x="2" y="5" width="20" height="14" fill="#2c4f5b"/>
        <path d="M2 5l10 8 10-8M2 19l7-7M22 19l-7-7" fill="none" stroke="#fff" stroke-width="1.5"/>
      </svg>
      Verdanixmedical.example
    </li>
    <li class="contact__item">
      <span class="contact__icon contact__icon--square"></span>
      verdanix_medical
    </li>
    <li class="contact__item contact__item--address">
      <svg class="contact__icon" viewBox="0 0 24 24" aria-hidden="true">
        <path fill="#2c4f5b" d="M12 2a7 7 0 0 0-7 7c0 5 7 13 7 13s7-8 7-13a7 7 0 0 0-7-7zm0 9.5A2.5 2.5 0 1 1 12 6.5a2.5 2.5 0 0 1 0 5z"/>
      </svg>
      <span>418 Harlan Brook Road<br>Suite 312 Alderwick<br>New York 11093</span>
    </li>
  </ul>
</section>

</body>
</html>
```